Microsite for a private healthcare provider

The design I need (PSD file) is for a company offering two services:
1. Recruitment of nurses
2. Provider a private health care: prenatal classes, vaccines for travellers
Here's a website we designed and we would like a similar style in terms of layout. Please note there will be about the same amount of content (text) http://lumivexstudio.ca/fr
Main menu with 4 sections:
Accueil |Agence de placement | Soins privés | Contact
Links to their social media accounts:
https://twitter.com/SoinsBrevalo
https://www.facebook.com/pages/SoinsBrevalo-Agence-de-placement-en-soins-de-sant%C3%A9/482913057264135
Contact details:
TÉL. (450) 555-0143
TÉLEC. (450) 555-0198
7186 boulevard Perrault, suite 1400
St-Hubert (Québec), J4X 1K3
Target Market(s)
Nurses looking for a job, Expecting women, People about to travel and seeking vaccines
Industry/Entity Type
Healthcare
Requirements
Must have
- 1- Must be responsive for mobiles and tablets
2 - Twitter feed
3 - Google maps at the end next to their contact details
4- Two contact forms:
Form for people to send in their resume.
The form title is: Postulez
Fields required:
Nom complet
Courriel
Téléphone
Années d'expérience (with drop down list: 1-2 ans, 3-5 ans, 5 ans et plus)
Choose file (possibility to attach a cv)
Message
Form for requesting information
Form title is: Demande d'informations
Fields are:
Nom complet
Téléphone
Courriel
Message
Nice to have
- Here are some images on Pixtura Foto the client likes, you can use for inspiration.
Agence de placement section:
File #40718253
File #6381947
File #5124086
File #8057291
File #30961472
File #27430685
File #45816037
Soins privés section:
File #36274519
File #49102853
File #31687240
File #25049716
File #43705128
File #38519602
File #29873154
File #7260835
File #34918657

```html
<!DOCTYPE html>
<html lang="fr">
<head>
<meta charset="utf-8">
<title>SoinsBrevalo – Soins de santé personnalisé, en privé</title>
<link href="https://fonts.googleapis.com/css2?family=Lato:wght@400;700;900&display=swap" rel="stylesheet">
<style>
:root{
  --blue:#1e54a3;
  --blue-dark:#163f7d;
  --green:#8ab43a;
  --green-dark:#6f9428;
  --page:#f4f4f4;
  --panel:#ffffff;
  --line:#d9d9d9;
  --text:#555a60;
  --heading:#2a2d31;
  --muted:#8a9096;
}
*{box-sizing:border-box;margin:0;padding:0}
html,body{width:1200px;height:2963px;overflow:hidden}
body{background:var(--page);font-family:'Lato',Arial,sans-serif;color:var(--text);position:relative}
section,header,nav,footer,.social-strip{position:relative;width:1200px;overflow:hidden}
.abs{position:absolute}

/* hero */
.hero{height:489px;background:linear-gradient(180deg,#e3e9ee 0%,#eef1f3 55%,#f1f1ef 100%)}
.hero-photo{position:absolute;inset:0;background:radial-gradient(ellipse at 20% 40%,#cdd9e2 0%,transparent 45%),radial-gradient(ellipse at 80% 45%,#d3dde4 0%,transparent 45%),radial-gradient(ellipse at 50% 90%,#dfe5e8 0%,transparent 60%)}
.hero-name{left:0;width:1200px;top:132px;text-align:center;font-weight:900;font-size:74px;color:var(--blue);letter-spacing:-1px}
.hero-tagline{left:0;width:1200px;top:236px;text-align:center;font-weight:700;font-size:25px;color:var(--blue)}
.hero-intro{left:311px;width:578px;top:282px;text-align:center;font-size:13px;line-height:18px;color:#4b5056}
.circle-btn{width:56px;height:56px;border-radius:50%;background:var(--green);display:flex;align-items:center;justify-content:center}
.hero .circle-btn{left:572px;top:396px}

/* social strip */
.social-strip{height:29px;background:#e4e4e2;border-bottom:1px solid #cfcfcf}
.strip-btn{top:6px;height:17px;padding:0 8px;background:#fff;border:1px solid #c9c9c9;border-radius:2px;font-size:9px;line-height:15px;color:#444;display:flex;align-items:center;gap:5px;white-space:nowrap}
.strip-btn i{width:9px;height:9px;background:var(--blue);display:block}

/* nav */
.main-nav{height:66px;background:var(--blue);border-top:2px solid #3b6fb9}
.nav-brand{left:237px;top:12px;color:#fff}
.nav-brand b{display:block;font-weight:900;font-size:24px;line-height:26px}
.nav-brand span{display:block;font-size:9px;line-height:12px}
.nav-menu{left:553px;top:0;height:64px;display:flex;list-style:none}
.nav-menu li{padding:0 13px;font-size:12px;font-weight:700;color:#fff;line-height:64px;text-transform:uppercase}
.nav-menu li.active{background:var(--blue-dark);border-bottom:3px solid var(--green)}

/* section titles */
.section-title{left:0;width:1200px;text-align:center;font-weight:900;font-size:36px;color:var(--heading);text-transform:uppercase}
.section-sub{left:0;width:1200px;text-align:center;font-size:12px;color:var(--blue)}
.title-rule{left:450px;width:300px;height:1px;background:var(--line)}

/* placement */
.placement{height:432px}
.placement-photo{left:246px;top:106px;width:281px;height:297px;background:linear-gradient(160deg,#e8eef3,#c7d9e8 50%,#e9cfd9);border:4px solid #fff;box-shadow:0 0 0 1px var(--line)}
.recruit-col{left:548px;top:108px;width:420px;display:flex;flex-direction:column}
.col-title{font-size:27px;line-height:32px;color:var(--blue);font-weight:400}
.body-text{font-size:12px;line-height:16px;color:var(--text)}
.points-title{font-size:15px;line-height:18px;color:var(--green);font-weight:700;margin-top:10px}
.points{list-style:none;display:grid;grid-template-columns:200px 200px;row-gap:6px;margin-top:8px}
.points li{display:flex;align-items:center;gap:8px;font-size:12px;line-height:14px;color:#555}
.points li svg{flex:none}
.btn{background:var(--green);color:#fff;font-weight:700;font-size:15px;border-radius:4px;display:flex;align-items:center;justify-content:center;box-shadow:inset 0 -3px 0 var(--green-dark)}

/* photo band */
.photo-band{background:linear-gradient(180deg,#c6d2dc,#dfe6ec 45%,#c9d4dc);}
.band-fill{position:absolute;inset:0;background:radial-gradient(ellipse at 15% 50%,#b7c6d2 0,transparent 40%),radial-gradient(ellipse at 85% 45%,#b9c8d3 0,transparent 40%)}
.band-line{height:1px;background:rgba(255,255,255,.85);width:190px}
.band-icon{width:52px;height:52px;border-radius:50%;border:3px solid #fff;display:flex;align-items:center;justify-content:center}

/* private */
.private{height:504px}
.private-icon{left:249px;top:148px;width:77px;height:77px;border-radius:50%;background:var(--green);display:flex;align-items:center;justify-content:center}
.private-col{left:344px;top:148px;width:256px;display:flex;flex-direction:column}
.small-head{font-size:11px;line-height:14px;font-weight:700;color:#444;text-transform:uppercase}
.private-col .body-text{font-size:11.5px;line-height:15px}
.private-photo{left:613px;top:133px;width:341px;height:341px;border-radius:50%;background:radial-gradient(circle at 45% 45%,#f4e1d8,#e6c6c0 55%,#d8d3dc);border:5px solid #fff;box-shadow:0 0 0 2px #ead5de}

/* contact */
.contact{height:500px}
.form-panel{top:154px;height:258px;background:var(--panel);border:1px solid var(--line);border-radius:3px;padding:10px 14px}
.form-title{font-size:14px;color:var(--blue);font-weight:700;padding-bottom:6px;border-bottom:1px solid var(--line);margin-bottom:8px}
.field{height:24px;border:1px solid #d6d6d6;background:#fbfbfb;font-size:11px;color:#666;padding:0 8px;line-height:22px;margin-bottom:6px;position:relative}
.field.area{height:52px}
.field.tall{height:120px}
.select-arrow{position:absolute;right:0;top:0;width:22px;height:22px;background:#e6e6e6;border-left:1px solid #d6d6d6}
.browse{position:absolute;right:-1px;top:-1px;height:24px;width:62px;background:#eef3f8;border:1px solid #c9d4df;font-size:10px;text-align:center;color:var(--blue)}
.submit{top:420px;width:132px;height:32px;font-size:14px}

/* locate */
.locate{height:493px}
.info-line{font-size:13px;color:#444;line-height:19px}
.info-head{font-size:17px;font-weight:700;color:#333}
.map{left:584px;top:93px;width:358px;height:198px;background:linear-gradient(135deg,#e9ecea,#dfe5dc 40%,#e8e4d6 70%,#dce3ea);border:5px solid #fff;box-shadow:0 0 0 1px var(--line)}
.badge{top:336px;height:44px;width:118px;border-radius:4px;display:flex;align-items:center;gap:8px;padding:0 10px;font-size:11px;font-weight:700}
.badge i{width:14px;height:14px;border-radius:50%;display:block;background:currentColor}
.tweets{left:584px;top:336px;width:370px;height:133px;background:#fff;border:1px solid var(--line)}
.tweets-head{height:26px;border-bottom:1px solid var(--line);display:flex;align-items:center;justify-content:space-between;padding:0 8px;font-size:11px;color:var(--blue);font-weight:700}
.follow{font-size:9px;color:#333;border:1px solid #ccc;background:#f3f3f3;padding:2px 6px;border-radius:2px;font-weight:400}
.tweet{display:flex;gap:10px;padding:9px 8px;border-bottom:1px solid #eee;font-size:10px;line-height:13px}
.tweet i{width:42px;height:28px;background:#dde6f2;display:block;flex:none}
.tweet b{color:var(--blue)}

/* footer */
.site-footer{height:50px;background:var(--blue)}
.footer-legal{left:246px;top:18px;font-size:10px;color:#dfe8f5;text-transform:uppercase}
.footer-top{left:900px;top:9px;display:flex;align-items:center;gap:8px;color:#fff;font-size:11px}
.footer-top span.ring{width:32px;height:32px;border-radius:50%;border:2px solid #fff;display:flex;align-items:center;justify-content:center}
</style>
</head>
<body>

<header class="hero">
  <div class="hero-photo" role="img" aria-label="Photo estompée d'une équipe médicale souriante"></div>
  <div class="abs hero-name">SoinsBrevalo</div>
  <div class="abs hero-tagline">Soins de sante personnalise, en prive</div>
  <p class="abs hero-intro">Lorem ipsum dolor sit amet, consectetur adipisicing elit, sed do eiusmod tempor incididunt ut labore et dolore magna aliqua. Ut enim ad minim veniam, quis nostrud exercitation ullamco laboris nisi ut aliquip ex ea commodo consequat. Reprehenderit in voluptate velit esse cillum dolore eu fugiat nulla pariatur. Lorem ipsum dolor sit amet, consectetur adipisicing elit, sed do eiusmod tempor incididunt ut labore et dolore magna aliqua.</p>
  <div class="abs circle-btn"><svg width="22" height="14" viewBox="0 0 22 14"><path d="M2 2l9 9 9-9" fill="none" stroke="#fff" stroke-width="3.5" stroke-linecap="round" stroke-linejoin="round"/></svg></div>
</header>

<div class="social-strip">
  <div class="abs strip-btn" style="left:746px"><i></i>Rejoignez-nous</div>
  <div class="abs strip-btn" style="left:856px"><i></i>Suivez @SoinsBrevalo</div>
</div>

<nav class="main-nav">
  <div class="abs nav-brand"><b>SoinsBrevalo</b><span>Soins de sante personnalise, en prive</span></div>
  <ul class="abs nav-menu">
    <li class="active">Accueil</li>
    <li>Agence de placement</li>
    <li>Soins privés</li>
    <li>Contactez</li>
  </ul>
</nav>

<section class="placement">
  <h2 class="abs section-title" style="top:18px">Agence de placement</h2>
  <p class="abs section-sub" style="top:62px">Lorem ipsum dolor sit amet, consectetur adipisicing elit</p>
  <div class="abs title-rule" style="top:82px"></div>
  <div class="abs placement-photo" role="img" aria-label="Photo d'un infirmier et d'une infirmière en uniforme, pouces levés"></div>
  <div class="abs recruit-col">
    <h3 class="col-title">Recrutement d Infirmieres</h3>
    <p class="body-text" style="margin-top:4px">Lorem ipsum dolor sit amet, consectetur adipisicing elit, sed do eiusmod tempor incididunt ut labore et dolore magna aliqua. Ut enim ad minim veniam, quis nostrud exercitation ullamco laboris nisi ut aliquip ex ea commodo consequat.</p>
    <h4 class="points-title">Some Points</h4>
    <ul class="points">
      <li><svg width="13" height="13"><circle cx="6.5" cy="6.5" r="6.5" fill="#8ab43a"/><path d="M3.5 6.8l2 2 4-4" fill="none" stroke="#fff" stroke-width="1.6"/></svg>Agency or Placement</li>
      <li><svg width="13" height="13"><circle cx="6.5" cy="6.5" r="6.5" fill="#8ab43a"/><path d="M3.5 6.8l2 2 4-4" fill="none" stroke="#fff" stroke-width="1.6"/></svg>Translated to English</li>
      <li><svg width="13" height="13"><circle cx="6.5" cy="6.5" r="6.5" fill="#8ab43a"/><path d="M3.5 6.8l2 2 4-4" fill="none" stroke="#fff" stroke-width="1.6"/></svg>Nursing Job</li>
      <li><svg width="13" height="13"><circle cx="6.5" cy="6.5" r="6.5" fill="#8ab43a"/><path d="M3.5 6.8l2 2 4-4" fill="none" stroke="#fff" stroke-width="1.6"/></svg>We Private Placement</li>
      <li><svg width="13" height="13"><circle cx="6.5" cy="6.5" r="6.5" fill="#8ab43a"/><path d="M3.5 6.8l2 2 4-4" fill="none" stroke="#fff" stroke-width="1.6"/></svg>Your Resume</li>
      <li><svg width="13" height="13"><circle cx="6.5" cy="6.5" r="6.5" fill="#8ab43a"/><path d="M3.5 6.8l2 2 4-4" fill="none" stroke="#fff" stroke-width="1.6"/></svg>Nursing Job</li>
      <li><svg width="13" height="13"><circle cx="6.5" cy="6.5" r="6.5" fill="#8ab43a"/><path d="M3.5 6.8l2 2 4-4" fill="none" stroke="#fff" stroke-width="1.6"/></svg>You can do it</li>
      <li><svg width="13" height="13"><circle cx="6.5" cy="6.5" r="6.5" fill="#8ab43a"/><path d="M3.5 6.8l2 2 4-4" fill="none" stroke="#fff" stroke-width="1.6"/></svg>Submit CV</li>
    </ul>
    <div class="btn" style="width:172px;height:40px;margin-top:14px">Contactez-nous</div>
  </div>
</section>

<section class="photo-band" style="height:199px">
  <div class="band-fill" role="img" aria-label="Bandeau photo estompé de personnel soignant"></div>
  <div class="abs band-line" style="left:370px;top:100px"></div>
  <div class="abs band-line" style="left:640px;top:100px"></div>
  <div class="abs band-icon" style="left:574px;top:75px"><svg width="20" height="13" viewBox="0 0 20 13"><path d="M2 11l8-8 8 8" fill="none" stroke="#fff" stroke-width="3.5" stroke-linecap="round" stroke-linejoin="round"/></svg></div>
</section>

<section class="private">
  <h2 class="abs section-title" style="top:40px">Soins de sante prives</h2>
  <p class="abs section-sub" style="top:86px">Lorem ipsum dolor sit amet, consectetur adipisicing elit</p>
  <div class="abs title-rule" style="top:106px"></div>
  <div class="abs private-icon"><svg width="42" height="32" viewBox="0 0 42 32"><circle cx="14" cy="9" r="7" fill="#fff"/><path d="M1 31c0-9 6-13 13-13s13 4 13 13z" fill="#fff"/><circle cx="29" cy="8" r="6" fill="#fff" opacity=".85"/><path d="M25 17c2-1 3-1 4-1 7 0 12 4 12 12h-11c0-5-2-9-5-11z" fill="#fff" opacity=".85"/></svg></div>
  <div class="abs private-col">
    <p class="small-head">About private health care practice</p>
    <p class="body-text" style="margin-top:5px">Lorem ipsum dolor sit amet, consectetur adipisicing elit, sed do eiusmod tempor incididunt ut labore et dolore magna aliqua. Ut enim ad minim veniam, quis nostrud exercitation ullamco laboris nisi ut aliquip ex ea commodo consequat.</p>
    <p class="small-head" style="margin-top:14px">Why choose us?</p>
    <p class="body-text" style="margin-top:5px">Lorem ipsum dolor sit amet, consectetur adipisicing elit, sed do eiusmod tempor incididunt ut labore et dolore magna aliqua.</p>
    <div class="btn" style="width:172px;height:40px;margin-top:22px">Contactez-nous</div>
  </div>
  <div class="abs private-photo" role="img" aria-label="Photo d'une mère tenant tendrement son nouveau-né"></div>
</section>

<section class="photo-band" style="height:201px">
  <div class="band-fill" role="img" aria-label="Bandeau photo estompé de personnel soignant"></div>
  <div class="abs band-line" style="left:370px;top:94px"></div>
  <div class="abs band-line" style="left:640px;top:94px"></div>
  <div class="abs band-icon" style="left:574px;top:68px"><svg width="20" height="13" viewBox="0 0 20 13"><path d="M2 11l8-8 8 8" fill="none" stroke="#fff" stroke-width="3.5" stroke-linecap="round" stroke-linejoin="round"/></svg></div>
</section>

<section class="contact">
  <h2 class="abs section-title" style="top:22px">Contact-nous</h2>
  <p class="abs section-sub" style="top:70px">Lorem ipsum dolor sit amet, consectetur adipisicing elit</p>
  <div class="abs title-rule" style="top:90px"></div>

  <form class="abs form-panel" style="left:246px;width:344px">
    <div class="form-title">Postulez</div>
    <div class="field">Nom complet</div>
    <div class="field">Courriel</div>
    <div class="field">Telephone</div>
    <div class="field">Années d'expérience<span class="select-arrow"><svg width="22" height="22"><path d="M7 9l4 4 4-4z" fill="#555"/></svg></span></div>
    <div class="field">Joindre CV<span class="browse">Parcourir</span></div>
    <div class="field area">Un Message</div>
  </form>
  <div class="abs btn submit" style="left:458px">Soumettre</div>

  <form class="abs form-panel" style="left:613px;width:341px">
    <div class="form-title">Demande d'informations</div>
    <div class="field">Nom complet</div>
    <div class="field">Courriel</div>
    <div class="field">Telephone</div>
    <div class="field tall">Message</div>
  </form>
  <div class="abs btn submit" style="left:822px">Soumettre</div>
</section>

<section class="locate">
  <h2 class="abs section-title" style="top:24px">Nous situer</h2>
  <div class="abs" style="left:258px;top:110px">
    <p class="info-line">TÉL. (450) 555-0143</p>
    <p class="info-line">TÉLEC. (450) 555-0198</p>
    <p class="info-head" style="margin-top:22px">Adresse</p>
    <p class="info-line" style="margin-top:6px">7186 boulevard Perrault, suite 1400</p>
    <p class="info-line">St-Hubert (Québec), J4X 1K3</p>
  </div>
  <div class="abs map" role="img" aria-label="Carte de localisation du bureau à St-Hubert"></div>

  <div class="abs badge" style="left:246px;background:#e4eef8;color:#2a88c8;border:1px solid #bcd3ea"><i></i>Suivez-nous</div>
  <div class="abs badge" style="left:372px;background:var(--blue);color:#fff"><i></i>Aimez-nous</div>

  <div class="tweets abs">
    <div class="tweets-head">Tweets<span class="follow">Suivre @SoinsBrevalo</span></div>
    <div class="tweet"><i></i><div><b>SoinsBrevalo @soinsbrevalo</b><br>Lorem ipsum dolor sit amet, consectetur adipisicing elit.</div></div>
    <div class="tweet"><i></i><div><b>SoinsBrevalo @soinsbrevalo</b><br>Lorem ipsum dolor sit amet, consectetur adipisicing elit.</div></div>
  </div>
</section>

<footer class="site-footer">
  <div class="abs footer-legal">SoinsBrevalo © 2013 | Privacy Policy</div>
  <div class="abs footer-top"><span class="ring"><svg width="14" height="9" viewBox="0 0 14 9"><path d="M2 7l5-5 5 5" fill="none" stroke="#fff" stroke-width="2.5" stroke-linecap="round"/></svg></span>Top</div>
</footer>

</body>
</html>
```